Business cards and logo for kitchen and bath remodeling company

We want an elegant card but that calls attention something unique and when people see it they remember us. A log that we can use for our own. We are a kitchen and bathroom remodeling company. We are 3 partners staring the company we are located in seattle washington usa. We try to give the best experience and luxury look in our projects and we are looking to show that in our cards. I added a sample of a card I really like. I like the black and gold look but gray blue or green in a metallic look would look nice. I'm open to any color.

Target Market(s)

Home owners.

Industry/Entity Type

Construction

Contact Information for Business Card

Larchmont and Vey builders

Colors

Designer to choose colors to be used in the design.

Requirements
Must have
• Make a Logo
• Logo to be unique
• Name of company larchmont and vey builders
Nice to have
• Have a good color scheme
• Front design to connect with back of card

```html
<!DOCTYPE html>
<html lang="en">
<head>
<meta charset="utf-8">
<title>Larchmont and Vey Builders – Business Card</title>
<link href="https://fonts.googleapis.com/css2?family=Montserrat:wght@500;600&family=Roboto:wght@400;500&display=swap" rel="stylesheet">
<style>
  :root {
    --backdrop: #8e8f8f;
    --card: #232323;
    --gold: #c6a22a;
    --silver: #d9d9d9;
    --card-w: 698px;
    --card-h: 386px;
  }
  * { box-sizing: border-box; margin: 0; padding: 0; }
  html, body { width: 1112px; height: 1200px; overflow: hidden; }
  body { background: var(--backdrop); position: relative; font-family: "Montserrat", sans-serif; }

  .card {
    position: absolute;
    left: 221px;
    width: var(--card-w);
    height: var(--card-h);
    background: var(--card);
  }
  .card--front { top: 159px; }
  .card--back { top: 629px; }

  .brand-mark {
    position: absolute;
    left: 50%;
    transform: translateX(-50%);
    display: flex;
    align-items: center;
    gap: 10px;
    white-space: nowrap;
    color: var(--gold);
    font-weight: 600;
    letter-spacing: 0.04em;
  }
  .brand-mark__square { width: 14px; height: 14px; background: var(--gold); flex: none; }
  .card--front .brand-mark { top: 78px; font-size: 21px; }
  .card--back .brand-mark { top: 159px; font-size: 23px; }

  .brand-title {
    position: absolute;
    left: 0; right: 0;
    text-align: center;
    color: var(--gold);
    font-weight: 500;
    letter-spacing: 0.02em;
    white-space: nowrap;
  }
  .card--front .brand-title { top: 132px; font-size: 25px; }
  .card--back .brand-title { top: 218px; font-size: 28.5px; }

  .person {
    position: absolute;
    right: calc(var(--card-w) - 326px);
    top: 213px;
    text-align: right;
  }
  .person__name { color: var(--gold); font-weight: 600; font-size: 24px; letter-spacing: 0.03em; word-spacing: 0.15em; line-height: 1.1; }
  .person__role { color: var(--silver); font-family: "Roboto", sans-serif; font-weight: 500; font-size: 19px; margin-top: 2px; }

  .divider { position: absolute; left: 347px; top: 204px; width: 1.5px; height: 67px; background: var(--gold); }

  .contacts {
    position: absolute;
    left: 367px;
    top: 203px;
    list-style: none;
    font-family: "Roboto", sans-serif;
    font-size: 17px;
    color: var(--silver);
  }
  .contacts li { display: flex; align-items: center; gap: 7px; height: 22.5px; }
  .contacts svg { width: 17px; height: 17px; fill: var(--gold); flex: none; }

  .company {
    position: absolute;
    left: 0; right: 0;
    top: 292px;
    text-align: center;
  }
  .company__name { color: var(--gold); font-weight: 600; font-size: 15px; letter-spacing: 0.02em; }
  .company__address { color: var(--silver); font-size: 15px; margin-top: 5px; letter-spacing: 0.02em; }
</style>
</head>
<body>
  <section class="card card--front" aria-label="Business card front">
    <div class="brand-mark"><span class="brand-mark__square"></span>LARCHMONT &amp; VEY</div>
    <h1 class="brand-title">LARCHMONT AND VEY BUILDERS</h1>

    <div class="person">
      <p class="person__name">OWEN CALLOWAY</p>
      <p class="person__role">Director</p>
    </div>
    <div class="divider"></div>

    <ul class="contacts">
      <li>
        <svg viewBox="0 0 24 24" aria-hidden="true"><path d="M3 9c0-3 4-5 9-5s9 2 9 5v2h-5V8.5c-1-.6-2.5-.9-4-.9s-3 .3-4 .9V11H3z"/><path d="M7 12h10l2 8H5z"/></svg>
        (206) 555-0148
      </li>
      <li>
        <svg viewBox="0 0 24 24" aria-hidden="true"><path d="M2 6h20v12H2z M3.5 7.5 12 13l8.5-5.5" fill="none" stroke="#c6a22a" stroke-width="2"/></svg>
        info@larchmontvey.com
      </li>
      <li>
        <svg viewBox="0 0 24 24" aria-hidden="true"><circle cx="12" cy="12" r="10" fill="none" stroke="#c6a22a" stroke-width="2"/><path d="M6 7c2 0 3 1 4 3s-1 3 0 5 2 4 1 6c-4-1-7-4-8-8 0-2 1-4 3-6zM14 4c2 1 2 3 4 3s2 3 1 5-3 1-4 0-2-4-1-8z"/></svg>
        www.larchmontvey.com
      </li>
    </ul>

    <div class="company">
      <p class="company__name">Larchmont and Vey builders Ltd.</p>
      <p class="company__address">48 Alder Crest Way, Suite 210 Seattle, WA 98104</p>
    </div>
  </section>

  <section class="card card--back" aria-label="Business card back">
    <div class="brand-mark"><span class="brand-mark__square"></span>LARCHMONT &amp; VEY</div>
    <h2 class="brand-title">LARCHMONT AND VEY BUILDERS</h2>
  </section>
</body>
</html>
```